New business logo / Business Card Design

My company provides Interim Management and consultancy, for Facilities Services. Covers any aspect of facilities management, including M&E, helpdesk, asset management, supplier relationships, catering, cleaning etc. Company provides innovative solutions to exceed client needs, drawing on years of experience. Initial thoughts on logo are attached below. Fits with RAG status on projects, red, amber and green, with logo design colours around moving services from amber to green.

Target Market(s)

Facilities Management clients and service providers

Industry/Entity Type

Business

Contact Information for Business Card

Company Name = k7Rventures Ltd My name on card = Derek Whitcombe, Director Mobile = 07516309842 Email = Derek@k7rventuresltd.co.uk Twitter = @k7Rventures Ltd

Font styles to use
Sans Serif

Colors
f37122
00a990

Requirements
Must have
• Logo to be evident, with some background image in reference to Facilities Management

```html
<!DOCTYPE html>
<html lang="en">
<head>
<meta charset="utf-8">
<title>k7Rventures Ltd – Business Card</title>
<link href="https://fonts.googleapis.com/css2?family=Didact+Gothic&family=Questrial&display=swap" rel="stylesheet">
<style>
  :root {
    --stage: #e6e6e6;
    --card: #fbfbfa;
    --ink: #3d3d3d;
    --ink-soft: #4a4a4a;
    --accent-green: #8aa83a;
    --band: rgba(62, 62, 62, 0.92);
    --photo-light: #eef0ee;
    --photo-mid: #c9c6b2;
    --photo-dark: #6e6c60;
  }
  html, body {
    margin: 0;
    padding: 0;
    width: 1200px;
    height: 1001px;
    overflow: hidden;
    background: var(--stage);
  }
  .canvas {
    position: relative;
    width: 1200px;
    height: 1001px;
    font-family: "Didact Gothic", "Questrial", sans-serif;
    color: var(--ink);
  }
  .card {
    position: absolute;
    left: 345px;
    width: 510px;
    height: 338px;
    background: var(--card);
    box-shadow: 0 2px 6px rgba(0,0,0,0.18);
    overflow: hidden;
  }
  .card--front { top: 134px; }
  .card--back  { top: 529px; }

  .brand-name {
    font-family: "Questrial", sans-serif;
    font-size: 34px;
    letter-spacing: -0.5px;
    white-space: nowrap;
    margin: 0;
    line-height: 1;
  }
  .card--front .brand-name {
    position: absolute;
    left: 39px;
    top: 66px;
    color: var(--ink);
  }

  .contact-list {
    position: absolute;
    left: 39px;
    top: 234px;
    margin: 0;
    padding: 0;
    list-style: none;
    font-size: 12.5px;
    line-height: 16.3px;
    color: var(--ink);
  }
  .contact-list li {
    display: flex;
    align-items: center;
    gap: 6px;
  }
  .contact-icon {
    width: 12px;
    height: 12px;
    flex: none;
  }

  .holder {
    position: absolute;
    right: 39px;
    top: 234px;
    text-align: right;
  }
  .holder-name {
    margin: 0;
    font-size: 15.5px;
    letter-spacing: 0.6px;
    text-transform: uppercase;
    font-weight: 700;
    color: var(--ink-soft);
    line-height: 1.1;
  }
  .holder-role {
    margin: 2px 0 0;
    font-size: 12.5px;
    color: var(--ink-soft);
  }

  .photo-fill {
    position: absolute;
    inset: 0;
    background:
      linear-gradient(160deg, var(--photo-light) 0%, #dfe2dc 35%, var(--photo-mid) 70%, var(--photo-dark) 100%);
  }
  .brand-band {
    position: absolute;
    left: 0;
    top: 134px;
    width: 286px;
    height: 70px;
    background: var(--band);
    display: flex;
    align-items: center;
  }
  .brand-band .brand-name {
    margin-left: 34px;
    color: #ffffff;
    font-size: 32px;
  }
</style>
</head>
<body>
<main class="canvas">

  <section class="card card--front" aria-label="Card front">
    <h1 class="brand-name">k7Rventures Ltd</h1>

    <ul class="contact-list">
      <li>
        <svg class="contact-icon" viewBox="0 0 12 12" aria-hidden="true">
          <rect width="12" height="12" rx="2" fill="var(--accent-green)"/>
          <rect x="3.5" y="2" width="5" height="8" rx="1" fill="none" stroke="#fff" stroke-width="1"/>
        </svg>
        07516309842
      </li>
      <li>
        <svg class="contact-icon" viewBox="0 0 12 12" aria-hidden="true">
          <rect width="12" height="12" rx="2" fill="var(--accent-green)"/>
        </svg>
        @k7Rventures Ltd
      </li>
      <li>
        <svg class="contact-icon" viewBox="0 0 12 12" aria-hidden="true">
          <rect width="12" height="12" rx="2" fill="var(--accent-green)"/>
          <rect x="2" y="3.5" width="8" height="5" fill="none" stroke="#fff" stroke-width="1"/>
          <path d="M2 3.5 L6 6.5 L10 3.5" fill="none" stroke="#fff" stroke-width="1"/>
        </svg>
        Derek@k7rventuresltd.co.uk
      </li>
      <li>
        <svg class="contact-icon" viewBox="0 0 12 12" aria-hidden="true">
          <rect width="12" height="12" rx="2" fill="var(--accent-green)"/>
          <circle cx="6" cy="6" r="3.8" fill="none" stroke="#fff" stroke-width="0.9"/>
          <ellipse cx="6" cy="6" rx="1.6" ry="3.8" fill="none" stroke="#fff" stroke-width="0.8"/>
          <line x1="2.2" y1="6" x2="9.8" y2="6" stroke="#fff" stroke-width="0.8"/>
        </svg>
        www.k7rventuresltd.co.uk
      </li>
    </ul>

    <div class="holder">
      <p class="holder-name">Derek Whitcombe</p>
      <p class="holder-role">Director</p>
    </div>
  </section>

  <section class="card card--back" aria-label="Card back">
    <div class="photo-fill" role="img" aria-label="Photo of two business people shaking hands on a glass-walled staircase in a modern office atrium"></div>
    <div class="brand-band">
      <p class="brand-name">k7Rventures Ltd</p>
    </div>
  </section>

</main>
</body>
</html>
```